July 4th Postcard to existing clients

5x7 postcard wishing our clients happy 4th of July. Card should read on the back "Thank You For Being A Valued Client!. Stay Safe And Enjoy Your Independence Day Celebrations!"

Patriotic theme with fireworks is ideal. We are a law firm so should still have a feel of professionalism while still being fun since it is for a fun holiday.

```html
<!DOCTYPE html>
<html lang="en">
<head>
<meta charset="utf-8">
<title>Independence Day Client Postcard</title>
<link rel="stylesheet" href="https://fonts.googleapis.com/css2?family=Roboto+Condensed:wght@700&family=Questrial&family=Montserrat:wght@400&display=swap">
<style>
  :root {
    --bg: #1b5b86;
    --navy: #26336b;
    --red: #c0282f;
    --band-red: #9e1f2a;
    --sky: #3a8fd0;
    --ink: #3a3a40;
    --line: #8a8fb2;
    --stamp: #e6e6ee;
    --white: #ffffff;
  }
  html, body {
    margin: 0;
    padding: 0;
    width: 1200px;
    height: 1200px;
    overflow: hidden;
    background: var(--bg);
  }
  .canvas { position: relative; width: 1200px; height: 1200px; }

  /* Front of postcard */
  .card-front {
    position: absolute;
    left: 60px; top: 50px;
    width: 738px; height: 526px;
    overflow: hidden;
    background: var(--white);
  }
  .crowd-photo {
    position: absolute; inset: 0;
    background: linear-gradient(180deg, #6b6f80 0%, #7a6a66 35%, #8a7e7c 55%, #d7dbe6 78%, #f3f4f8 100%);
  }
  .flag-wave {
    position: absolute; left: 0; right: 0; bottom: 0; height: 230px;
    background:
      linear-gradient(90deg, rgba(40,110,190,.85) 0%, rgba(120,180,230,.35) 30%, rgba(255,255,255,0) 50%, rgba(230,120,130,.35) 70%, rgba(190,40,50,.85) 100%),
      linear-gradient(180deg, rgba(255,255,255,0) 0%, rgba(255,255,255,.6) 40%, rgba(220,80,90,.5) 80%, rgba(200,50,60,.7) 100%);
  }
  .front-headline {
    position: absolute; left: 0; right: 0;
    text-align: center;
    font-family: 'Roboto Condensed', sans-serif;
    font-weight: 700;
    margin: 0;
  }
  .front-date { top: 278px; left: -20px; font-size: 38px; color: var(--navy); }
  .front-date sup { font-size: 20px; }
  .front-happy { top: 332px; left: -20px; font-size: 62px; color: var(--navy); letter-spacing: 1px; }
  .front-holiday { top: 407px; left: -20px; font-size: 38px; color: var(--red); }
  .country-band {
    position: absolute; left: 0; right: 0; top: 478px; height: 16px;
    background: linear-gradient(90deg, var(--band-red), #c23a44 50%, var(--band-red));
    color: var(--white);
    font-family: 'Montserrat', sans-serif;
    font-size: 13px; letter-spacing: 11px;
    line-height: 16px;
    padding-left: 92px;
    box-sizing: border-box;
  }
  .front-footer {
    position: absolute; left: 0; right: 0; top: 494px; bottom: 0;
    background: linear-gradient(90deg, var(--sky), #a9cdec 45%, #e08a92 75%, var(--red));
  }

  /* Back of postcard */
  .card-back {
    position: absolute;
    left: 355px; top: 608px;
    width: 739px; height: 528px;
    overflow: hidden;
    background: linear-gradient(170deg, #ea9cc2 0%, #f3d2e2 22%, #ffffff 50%, #f7f9fd 75%, #cfe3f5 100%);
  }
  .flags-photo {
    position: absolute; left: 0; top: 312px; width: 390px; height: 216px;
    background: linear-gradient(180deg, rgba(205,215,235,0) 0%, rgba(200,190,215,.55) 45%, rgba(185,200,225,.7) 100%);
  }
  .stamp-box {
    position: absolute; left: 606px; top: 38px; width: 91px; height: 90px;
    background: var(--stamp);
  }
  .firm-name {
    position: absolute; left: 0; width: 382px; top: 174px;
    margin: 0; text-align: center;
    font-family: 'Montserrat', sans-serif; font-weight: 400;
    font-size: 33px; letter-spacing: 2px; color: var(--ink);
  }
  .greeting {
    position: absolute; left: 0; width: 382px; top: 228px;
    margin: 0; text-align: center;
    font-family: 'Questrial', sans-serif;
    color: var(--ink); font-size: 19px; line-height: 24px;
  }
  .greeting .spacer { display: block; height: 24px; }
  .greeting .holiday { display: block; font-size: 29px; line-height: 32px; margin-top: 2px; }
  .address-line {
    position: absolute; left: 425px; width: 273px; height: 2px;
    background: var(--line);
  }
</style>
</head>
<body>
<div class="canvas">

  <section class="card-front">
    <div class="crowd-photo" role="img" aria-label="Photo of a smiling, diverse crowd waving small American flags"></div>
    <div class="flag-wave" role="img" aria-label="Sweeping American flag waves with stars in red, white and blue"></div>
    <p class="front-headline front-date">4<sup>th</sup> july</p>
    <p class="front-headline front-happy">HAPPY</p>
    <p class="front-headline front-holiday">INDEPENDENCE DAY</p>
    <div class="country-band">UNITED STATES OF AMERICA</div>
    <div class="front-footer"></div>
  </section>

  <section class="card-back">
    <div class="flags-photo" role="img" aria-label="Faded photo of raised hands holding American flags"></div>
    <div class="stamp-box"></div>
    <h1 class="firm-name">HARWELL LAW</h1>
    <p class="greeting">
      Thank You For<br>
      Being A Valued Client!.
      <span class="spacer"></span>
      Stay Safe And<br>
      Enjoy Your
      <span class="holiday">Independence Day</span>
      Celebrations!
    </p>
    <div class="address-line" style="top:245px"></div>
    <div class="address-line" style="top:284px"></div>
    <div class="address-line" style="top:324px"></div>
    <div class="address-line" style="top:366px"></div>
    <div class="address-line" style="top:410px"></div>
  </section>

</div>
</body>
</html>
```